Simple but elegant business card/logo design for exclusive beauty business

We need a logo designed for a new elegant and exclusive beauty business called "R". The logo itself should be a stylistic and custom design for the letter "R". We would like the business card to have the logo as the centrepiece on a clean background. Gold Logo on black background or silver on white background.

The business card details should be displayed centre of the card. Details are as follows:

Tamsin Earle
Faceline: /shinesoftlyr
Photogram: /shinesoftlyr

The words "Shine Softly" should also appear somewhere on the card.

Industry/Entity Type

Business

Logo Text

G

Requirements
Must have
• Design must be simple, clean and elegant
Should not have
• The design should not be cluttered

```html
<!DOCTYPE html>
<html lang="en">
<head>
<meta charset="utf-8">
<title>Tamsin Earle – Business Cards</title>
<link href="https://fonts.googleapis.com/css2?family=Open+Sans:wght@400;600&family=Pinyon+Script&display=swap" rel="stylesheet">
<style>
  :root {
    --backdrop: #353535;
    --card-light: #e6e5e3;
    --card-green: #72a556;
    --brand-green: #6ea558;
    --mark-silver: #8a8a8a;
    --rule-grey: #9a9a9a;
    --ink: #2f2f2f;
    --white: #ffffff;
  }
  * { margin: 0; padding: 0; box-sizing: border-box; }
  html, body {
    width: 1200px; height: 900px; overflow: hidden;
    background: var(--backdrop);
    font-family: "Open Sans", Arial, sans-serif;
  }
  .stage { position: relative; width: 1200px; height: 900px; }
  .card {
    position: absolute; top: 170px; width: 347px; height: 561px;
    box-shadow: 2px 3px 4px rgba(0,0,0,0.45);
  }
  .card--front { left: 259px; background: var(--card-light); }
  .card--back { left: 631px; background: var(--card-green); }

  .brand-mark {
    position: absolute; left: 0; width: 100%; text-align: center;
    font-family: "Open Sans", Arial, sans-serif; font-weight: 400;
    line-height: 1;
  }
  .card--front .brand-mark { top: 120px; font-size: 170px; color: var(--mark-silver); }
  .card--back .brand-mark { top: 160px; font-size: 190px; color: var(--white); }

  .holder-name {
    position: absolute; top: 374px; left: 0; width: 100%; text-align: center;
    font-size: 24px; font-weight: 600; color: var(--brand-green); letter-spacing: 0.3px;
  }
  .divider {
    position: absolute; top: 426px; left: 99px; width: 149px; height: 1px;
    background: var(--rule-grey);
  }
  .social-list {
    position: absolute; top: 454px; left: 0; width: 100%;
    display: flex; justify-content: center; gap: 14px;
    font-size: 12px; font-weight: 600; color: var(--brand-green);
  }
  .social-item { display: flex; align-items: center; gap: 5px; }
  .social-dot { width: 12px; height: 12px; border-radius: 50%; background: var(--brand-green); }
  .handle {
    position: absolute; top: 488px; left: 0; width: 100%; text-align: center;
    font-size: 20px; font-weight: 400; color: var(--ink);
  }
  .tagline {
    position: absolute; top: 455px; left: 0; width: 100%; text-align: center;
    font-family: "Pinyon Script", cursive; font-size: 40px; color: var(--white);
  }
</style>
</head>
<body>
<main class="stage">
  <section class="card card--front">
    <div class="brand-mark">R</div>
    <h1 class="holder-name">TAMSIN EARLE</h1>
    <div class="divider"></div>
    <div class="social-list">
      <span class="social-item"><span class="social-dot"></span>Faceline</span>
      <span class="social-item"><span class="social-dot"></span>Photogram</span>
    </div>
    <p class="handle">/shinesoftlyr</p>
  </section>
  <section class="card card--back">
    <div class="brand-mark">R</div>
    <p class="tagline">Shine Softly</p>
  </section>
</main>
</body>
</html>
```